regPersonal Trainer Flyer Design

Reason: I have been very busy with other work and would like to extend the deadline to offer designers the chance to edit and improve designs with my help. Thank you for all the designs that have been sent so far.

```html
<!DOCTYPE html>
<html lang="en">
<head>
<meta charset="utf-8">
<title>Personal Trainer Flyer</title>
<link rel="stylesheet" href="https://fonts.googleapis.com/css2?family=Comic+Neue:ital,wght@0,400;0,700;1,400;1,700&display=swap">
<style>
:root{
  --page:#ececec;
  --paper:#f7f7f6;
  --navy:#0b5696;
  --deep:#084a85;
  --mid:#2f8ed6;
  --sky:#a3d5f1;
  --ink:#141414;
  --white:#ffffff;
  --cream:#fff2a6;
}
*{margin:0;padding:0;box-sizing:border-box}
html,body{width:1200px;height:1000px;overflow:hidden;background:var(--page)}
body{position:relative;font-family:"Comic Neue",cursive}
.flyer{
  position:absolute;left:27px;top:94px;width:970px;height:687px;
  transform:scale(1.18);transform-origin:0 0;
  background:var(--paper);overflow:hidden;
  box-shadow:0 4px 14px rgba(0,0,0,.18);
}
.stripes{position:absolute;inset:0}
.headline{
  position:absolute;left:110px;top:30px;width:300px;text-align:center;color:var(--white);line-height:1.1;
}
.headline .soft{font-size:30px;font-style:italic;display:block}
.headline .strong{font-size:42px;font-weight:700;font-style:italic;display:block}
.headline .easier{font-weight:700;font-size:38px}
.photo{position:absolute;border:3px solid var(--white);box-shadow:0 1px 3px rgba(0,0,0,.3)}
.photo-lifter{left:33px;top:188px;width:396px;height:252px;background:linear-gradient(135deg,#9c4a32,#7a3a2a 45%,#2a2a2a 70%,#b5573b)}
.photo-session{left:698px;top:451px;width:216px;height:157px;background:linear-gradient(135deg,#d9dde2,#8b8f96 45%,#3a3230 70%,#c9c4c0)}
.pitch{
  position:absolute;left:20px;top:464px;width:290px;text-align:center;color:var(--white);
  font-size:24px;line-height:1.3;font-style:italic;
}
.pitch b{font-weight:700}
.benefits{position:absolute;list-style:none;color:var(--ink);font-size:21px;font-style:italic;line-height:1.2}
.benefits li{position:absolute;white-space:nowrap;padding-left:26px}
.benefits li::before{
  content:"";position:absolute;left:2px;top:8px;width:10px;height:10px;border-radius:50%;background:var(--navy);
}
.offer{position:absolute;left:735px;top:86px;width:230px;height:232px}
.offer-text{position:absolute;left:740px;top:156px;width:210px;text-align:center;font-weight:700;font-style:italic;line-height:1.2}
.offer-text .tag{color:var(--cream);font-size:27px;display:block}
.offer-text .deal{color:var(--white);font-size:28px;display:block;margin-top:8px}
.contact{position:absolute;left:420px;top:406px;width:260px;text-align:center;color:var(--navy);font-size:29px;font-weight:700;font-style:italic;text-decoration:underline;text-underline-offset:4px}
.trainer-name{position:absolute;left:380px;top:458px;width:330px;text-align:center;font-size:36px;font-weight:700;font-style:italic;color:var(--ink)}
.trainer-role{position:absolute;left:380px;top:510px;width:330px;text-align:center;font-size:25px;font-style:italic;color:var(--ink)}
.contact-line{position:absolute;display:flex;align-items:center;gap:12px;font-size:22px;font-style:italic;color:var(--ink)}
.contact-line svg{flex:none}
.phone{left:380px;top:562px}
.email{left:360px;top:618px}
</style>
</head>
<body>
<main class="flyer">
  <svg class="stripes" width="970" height="687" viewBox="0 0 970 687" aria-hidden="true">
    <g>
      <polygon points="0,0 14,0 -123,687 -137,687" fill="var(--sky)"/>
      <polygon points="30,0 48,0 -89,687 -107,687" fill="var(--mid)"/>
      <polygon points="58,0 68,0 -69,687 -79,687" fill="var(--deep)"/>
      <polygon points="80,0 92,0 -45,687 -57,687" fill="var(--sky)"/>
      <polygon points="100,0 440,0 303,687 -37,687" fill="var(--navy)"/>
      <polygon points="450,0 466,0 329,687 313,687" fill="var(--mid)"/>
      <polygon points="474,0 494,0 357,687 337,687" fill="var(--sky)"/>
      <polygon points="800,0 810,0 673,687 663,687" fill="var(--sky)"/>
      <polygon points="826,0 842,0 705,687 689,687" fill="var(--mid)"/>
      <polygon points="855,0 1200,0 1063,687 718,687" fill="var(--navy)"/>
      <polygon points="1060,0 1072,0 935,687 923,687" fill="var(--white)"/>
      <polygon points="1080,0 1096,0 959,687 943,687" fill="var(--sky)"/>
      <polygon points="1104,0 1112,0 975,687 967,687" fill="var(--white)"/>
    </g>
  </svg>

  <h1 class="headline">
    <span class="soft">Achieving your</span>
    <span class="strong">fitness goals</span>
    <span class="soft">just got <span class="easier">easier.</span></span>
  </h1>

  <div class="photo photo-lifter" role="img" aria-label="Photo of the trainer holding a barbell across his shoulders in front of a brick wall"></div>

  <p class="pitch">Need a personal trainer to improving <b>Fitness, Health, Posture</b>, or Recover from an <b>Injury</b> or complete a&nbsp; <b>Marathon</b>?</p>

  <ul class="benefits">
    <li style="left:492px;top:30px">Lacking motivation?</li>
    <li style="left:483px;top:66px">Not achieving your goals?</li>
    <li style="left:476px;top:103px">Need help?</li>
    <li style="left:467px;top:139px">Bored of the gym?</li>
    <li style="left:460px;top:175px">You're never too old.</li>
    <li style="left:452px;top:214px">I can help improve your<br>health and well-being.</li>
    <li style="left:443px;top:279px">Training can be at your<br>home.</li>
  </ul>

  <svg class="offer" viewBox="0 0 230 232" aria-hidden="true">
    <polygon points="12,56 100,2 100,56" fill="var(--deep)"/>
    <polygon points="22,54 230,54 212,230 0,230" fill="var(--navy)" stroke="var(--deep)" stroke-width="2"/>
  </svg>
  <div class="offer-text">
    <span class="tag">Introductory<br>- Offer -</span>
    <span class="deal">One free<br>session*</span>
  </div>

  <h2 class="contact">CONTACT</h2>
  <p class="trainer-name">Sam Keller</p>
  <p class="trainer-role">( Personal Trainer )</p>

  <p class="contact-line phone">
    <svg width="36" height="36" viewBox="0 0 36 36" aria-hidden="true">
      <circle cx="18" cy="18" r="18" fill="var(--navy)"/>
      <path d="M12 9c1-1 2-1 3 0l2 3c.6 1 .4 1.8-.4 2.5l-1 .8c.8 2 2.4 3.8 4.5 4.8l.9-1c.7-.8 1.6-.9 2.5-.3l3 2c1 .7 1 1.7 0 2.7l-1.5 1.5c-1.5 1.5-5 .5-8.5-3S9 13 10.5 10.5z" fill="var(--white)"/>
    </svg>
    07700 900412
  </p>
  <p class="contact-line email">
    <svg width="36" height="36" viewBox="0 0 36 36" aria-hidden="true">
      <circle cx="18" cy="18" r="18" fill="var(--navy)"/>
      <rect x="8" y="11" width="20" height="14" rx="1" fill="var(--white)"/>
      <path d="M8.5 11.5 18 19l9.5-7.5" fill="none" stroke="var(--navy)" stroke-width="1.6"/>
    </svg>
    samkeller@example.co.uk
  </p>

  <div class="photo photo-session" role="img" aria-label="Photo of the trainer spotting a client during a barbell squat in a gym"></div>
</main>
</body>
</html>
```